Business Card Design for Photographer

Updating business card design. Must use included logo. We're a luxury wedding photography business. Elegancy, luxury, consistency are messages we wish to convey.

Visit our website at www.colbyvarnway.com to familiarize yourself more with our brand design currently (fonts, colors etc.). This is what we want to maintain.

Target Market(s)

Luxury Brides and Grooms

Industry/Entity Type

Wedding

Contact Information for Business Card

Current logo (attached to brief)
Name: Colby Varnway
Phone: 5208813047
website/blog
Email

Requirements
Must have
• Current logo (attached to brief)
• Name: Colby Varnway
• Phone: 5208813047
• website/blog
• Email
• Instagram username
Should not have
• bright colors, fonts that don't suit our brand (visit www.colbyvarnway.com)

```html
<!DOCTYPE html>
<html lang="en">
<head>
<meta charset="utf-8">
<title>Colby Varnway Photographers – Business Card</title>
<link rel="stylesheet" href="https://fonts.googleapis.com/css2?family=Quicksand:wght@300;400;500;700&display=swap">
<style>
  :root {
    --page-bg: #e6e4e1;
    --card-light: #ececec;
    --card-light-edge: #f6f6f6;
    --card-dark: #2b2b2b;
    --card-dark-edge: #353535;
    --ink-grey: #6f6f6f;
    --ink-dark: #4a4a4a;
    --ink-white: #f2f2f2;
    --mark-grey: #555555;
  }
  * { margin: 0; padding: 0; box-sizing: border-box; }
  html, body {
    width: 1200px;
    height: 900px;
    overflow: hidden;
    background: var(--page-bg);
    font-family: "Quicksand", sans-serif;
  }
  .sheet {
    width: 1200px;
    height: 900px;
    display: flex;
    flex-direction: column;
    align-items: center;
    justify-content: center;
    gap: 44px;
  }
  .card {
    width: 660px;
    height: 377px;
    position: relative;
    box-shadow: 0 6px 18px rgba(0,0,0,0.18);
  }

  /* Front face */
  .card--front {
    background: linear-gradient(135deg, var(--card-light-edge), var(--card-light));
    color: var(--ink-grey);
  }
  .brand {
    position: absolute;
    left: 238px;
    top: 92px;
    display: flex;
    align-items: flex-start;
    gap: 20px;
  }
  .brand__words { text-align: left; }
  .brand__name {
    font-weight: 400;
    font-size: 22px;
    letter-spacing: 0.32em;
    color: var(--ink-grey);
  }
  .brand__tagline {
    margin-top: 6px;
    font-weight: 400;
    font-size: 12px;
    letter-spacing: 0.62em;
    color: var(--ink-grey);
  }
  .brand__square {
    width: 42px;
    height: 42px;
    background: var(--mark-grey);
    margin-top: -12px;
  }
  .contact {
    position: absolute;
    left: 64px;
    top: 150px;
    font-size: 16px;
    color: var(--ink-grey);
  }
  .contact__row { display: flex; gap: 26px; align-items: baseline; }
  .contact__label { font-weight: 500; width: 54px; }
  .contact__value { font-weight: 400; letter-spacing: 0.06em; }
  .contact__person {
    margin: 22px 0 22px 120px;
    font-weight: 700;
    font-size: 22px;
    letter-spacing: 0.05em;
    color: var(--ink-dark);
  }
  .contact__row--email { margin-left: 120px; }
  .contact__row--email .contact__value { margin-left: 0; }

  /* Back face */
  .card--back {
    background: linear-gradient(135deg, var(--card-dark), var(--card-dark-edge));
    color: var(--ink-white);
  }
  .links {
    position: absolute;
    left: 56px;
    top: 44px;
    display: flex;
    flex-direction: column;
    gap: 16px;
    font-size: 15px;
    letter-spacing: 0.04em;
  }
  .links__item { display: flex; align-items: center; gap: 16px; }
  .links__dot {
    width: 22px;
    height: 22px;
    border-radius: 50%;
    background: var(--ink-white);
  }
</style>
</head>
<body>
<main class="sheet">

  <section class="card card--front" aria-label="Business card front">
    <div class="brand">
      <div class="brand__words">
        <p class="brand__name">COLBY VARNWAY</p>
        <p class="brand__tagline">PHOTOGRAPHERS</p>
      </div>
      <div class="brand__square" aria-hidden="true"></div>
    </div>

    <div class="contact">
      <p class="contact__row">
        <span class="contact__label">Phone</span>
        <span class="contact__value">5208813047</span>
      </p>
      <p class="contact__person">Colby Varnway</p>
      <p class="contact__row">
        <span class="contact__label">Email</span>
        <span class="contact__value">hello@colbyvarnway.com</span>
      </p>
    </div>
  </section>

  <section class="card card--back" aria-label="Business card back">
    <div class="links">
      <p class="links__item"><span class="links__dot" aria-hidden="true"></span>Colby Varnway</p>
      <p class="links__item"><span class="links__dot" aria-hidden="true"></span>www.colbyvarnway.com</p>
    </div>
  </section>

</main>
</body>
</html>
```